Buntes und kreatives Etiketten-Design für Frühlingswein
Zielgruppe
Wir sind ein Getränke Fachgroßhändler im Norden und möchten eine kreatives Etikett unter dem wir unsere Flur Wein Eigenmarke vermarkte können.
Zielgruppe Gastronomie / Restaurant und Hotels
Aufgabenstellung
Wir benötigen ein Vorderetikett (Rückenetikett vorhanden)
Maße 80mm x 80 mm
Leichter Frühlingswein um bei den ersten Sonnenstrahlen es zu genießen.
Wir hätten gerne ein Etikett welches bunt, kreativ, innovativ und trinkanimierend ist. Es sollte in Anlehnung an die letzten zwei Etiketten sein.
Der Name Wendula sollte auf dem Etikett stehen
Im Anhang finden Sie die Etiketten aus den letzten zwei Jahren.
Wir haben diesen Wein bei verschiedenen Winzern füllen lassen und jedes Jahr ein neues Etikett.

```html
<!DOCTYPE html>
<html lang="de">
<head>
<meta charset="utf-8">
<title>Wendula – Frühlingswein Etikett</title>
<link rel="stylesheet" href="https://fonts.googleapis.com/css2?family=Open+Sans:wght@300&display=swap">
<style>
  :root {
    --page: #ffffff;
    --ink: #1c1a1a;
    --ink-soft: #3a3636;
    --sun: #f9e03a;
    --sun-deep: #f7c52c;
    --rose: #ea3f86;
    --rose-soft: #f4a3c6;
    --teal: #3cb7a4;
    --sky: #8fd3e3;
    --mist: #eef6ea;
    --portrait: #f7f5f2;
  }
  * { margin: 0; padding: 0; box-sizing: border-box; }
  html, body {
    width: 1200px;
    height: 800px;
    overflow: hidden;
    background: var(--page);
  }
  .canvas {
    position: relative;
    width: 1200px;
    height: 800px;
  }
  .label {
    position: absolute;
    left: 280px;
    top: 80px;
    width: 640px;
    height: 640px;
    overflow: hidden;
  }
  .label__wash {
    position: absolute;
    inset: 0;
    background:
      radial-gradient(ellipse 45% 40% at 80% 30%, var(--rose) 0%, transparent 70%),
      radial-gradient(ellipse 35% 45% at 95% 70%, var(--rose-soft) 0%, transparent 75%),
      radial-gradient(ellipse 45% 30% at 45% 62%, var(--teal) 0%, transparent 75%),
      radial-gradient(ellipse 55% 30% at 55% 95%, var(--sky) 0%, transparent 80%),
      radial-gradient(ellipse 40% 30% at 10% 90%, var(--mist) 0%, transparent 80%),
      linear-gradient(160deg, var(--sun) 0%, var(--sun-deep) 45%, var(--sun) 70%, var(--mist) 100%);
  }
  .label__portrait {
    position: absolute;
    left: 166px;
    top: 89px;
    width: 270px;
    height: 270px;
    border-radius: 50%;
    background: radial-gradient(circle at 50% 40%, var(--portrait) 0%, #e9e6e1 100%);
    border: 2px solid var(--ink);
  }
  .label__name {
    position: absolute;
    left: 0;
    right: 0;
    top: 400px;
    text-align: center;
    font-family: "Open Sans", sans-serif;
    font-weight: 300;
    font-size: 132px;
    line-height: 1;
    color: var(--ink);
    transform: rotate(-5deg);
  }
  .label__tagline {
    position: absolute;
    left: 128px;
    top: 548px;
    font-family: "Open Sans", sans-serif;
    font-weight: 300;
    font-size: 32px;
    letter-spacing: 2px;
    color: var(--ink-soft);
    white-space: nowrap;
    transform: rotate(-4deg);
    transform-origin: left center;
  }
</style>
</head>
<body>
  <main class="canvas">
    <section class="label" aria-label="Weinetikett Wendula">
      <div class="label__wash" role="img" aria-label="Bunter Aquarell-Hintergrund in Gelb, Pink, Türkis und Hellblau"></div>
      <div class="label__portrait" role="img" aria-label="Gezeichnete junge Frau mit Mütze und wehendem Haar, mit kleinen Blüten ringsum"></div>
      <h1 class="label__name">Wendula</h1>
      <p class="label__tagline">leicht · fruchtig · lecker</p>
    </section>
  </main>
</body>
</html>
```